Harbor Crew Biz Cards

looking for a new catchy business card where my cell number is very prominent:
My pic and logo are attached. My whole picture isn't necessary if it makes more sense to crop it.

Info needed:

(Big) Marcus Pellton
(Medium) Real Estate Professional
(Medium) Buyer/Seller Specialist
(Big) Call/Text 410-739-2184
(small) Marcuspell@mailbrook.com
(small) www.harborcrewhomes.com

(very small)
The Harbor Crew
at Keystone Real Estate
2847 W Larkmoor Rd, Bel Air, MD 21014
833-555-0192

```html
<!DOCTYPE html>
<html lang="en">
<head>
<meta charset="utf-8">
<title>Marcus Pellton – Business Card</title>
<link rel="stylesheet" href="https://fonts.googleapis.com/css2?family=Poppins:wght@700;800&family=Figtree:wght@400;500&family=Montserrat:wght@400;500;600&family=Lexend:wght@400;700&display=swap">
<style>
  :root {
    --navy: #0e2f5c;
    --navy-deep: #0d2d58;
    --sky-light: #6ba5ca;
    --sky-mid: #5b93bd;
    --sky-edge: #4a7eaa;
    --white: #ffffff;
    --suit-dark: #1f2840;
    --suit-mid: #2f3a58;
    --shadow-soft: rgba(255,255,255,0.35);
  }
  * { margin: 0; padding: 0; box-sizing: border-box; }
  html, body { width: 1200px; height: 686px; overflow: hidden; background: var(--sky-mid); }
  .card {
    position: relative;
    width: 1200px;
    height: 686px;
    overflow: hidden;
    background: radial-gradient(ellipse at 60% 45%, var(--sky-light) 0%, var(--sky-mid) 55%, var(--sky-edge) 100%);
  }
  .accent-lines { position: absolute; inset: 0; }
  .agent-photo {
    position: absolute;
    left: 20px; top: 30px;
    width: 306px; height: 625px;
    border-radius: 110px 110px 0 0;
    background: linear-gradient(180deg, var(--suit-mid) 0%, var(--suit-dark) 100%);
  }
  .agent-name {
    position: absolute;
    left: 344px; top: 52px;
    font-family: "Poppins", sans-serif;
    font-weight: 800;
    font-size: 94px;
    letter-spacing: -2px;
    line-height: 1;
    color: var(--navy);
    text-shadow: 4px 4px 0 var(--shadow-soft);
    white-space: nowrap;
  }
  .agent-titles {
    position: absolute;
    left: 346px; top: 150px;
    font-family: "Figtree", sans-serif;
    font-size: 29.5px;
    color: var(--white);
    white-space: nowrap;
  }
  .agent-titles .sep { margin: 0 18px; font-size: 20px; vertical-align: middle; }
  .contact-row {
    position: absolute;
    left: 438px;
    display: flex;
    align-items: center;
  }
  .contact-row svg { width: 30px; height: 30px; flex: none; }
  .contact-row .divider { width: 2px; height: 42px; background: var(--white); margin: 0 16px; flex: none; }
  .contact-row .value {
    font-family: "Montserrat", sans-serif;
    font-size: 28px;
    letter-spacing: 0.5px;
    white-space: nowrap;
  }
  .row-phone { top: 228px; }
  .row-phone svg { width: 36px; height: 36px; }
  .row-phone .divider { height: 56px; }
  .row-phone .value { color: var(--navy); font-weight: 600; font-size: 40px; letter-spacing: 0; }
  .row-phone .label { font-weight: 500; color: var(--white); margin-right: 10px; }
  .row-email { top: 304px; }
  .row-email .value { color: var(--white); }
  .row-web { top: 360px; }
  .row-web .value { color: var(--navy); font-weight: 500; letter-spacing: 1.5px; }
  .brand-mark {
    position: absolute;
    left: 460px; top: 462px;
    width: 200px; height: 180px;
    display: flex; align-items: center; justify-content: center;
    gap: 10px;
  }
  .brand-mark .dot { width: 18px; height: 18px; border-radius: 50%; background: var(--navy); flex: none; }
  .brand-mark .brand-name {
    font-family: "Lexend", sans-serif;
    font-weight: 700;
    font-size: 24px;
    color: var(--navy);
    white-space: nowrap;
  }
  .office {
    position: absolute;
    left: 694px; top: 452px;
    font-family: "Lexend", sans-serif;
    white-space: nowrap;
  }
  .office-team { font-weight: 700; font-size: 39px; color: var(--navy); line-height: 1.05; }
  .office-brokerage { font-size: 22px; color: var(--white); margin-top: 2px; }
  .office-address { font-size: 22.5px; color: var(--navy); margin-top: 22px; }
  .office-phone { font-size: 22.5px; color: var(--navy); margin-top: 8px; letter-spacing: 1px; }
  .footer-band {
    position: absolute;
    left: 0; bottom: 0;
    width: 1200px; height: 31px;
    background: var(--navy-deep);
  }
</style>
</head>
<body>
<main class="card">
  <svg class="accent-lines" width="1200" height="686" viewBox="0 0 1200 686" aria-hidden="true">
    <g stroke="#ffffff" stroke-opacity="0.25" stroke-width="1.5" fill="none">
      <line x1="0" y1="80" x2="140" y2="0"/>
      <line x1="0" y1="330" x2="580" y2="0"/>
      <line x1="0" y1="520" x2="330" y2="330"/>
      <line x1="600" y1="250" x2="1200" y2="-90"/>
      <line x1="1030" y1="660" x2="1200" y2="560"/>
      <line x1="880" y1="420" x2="1200" y2="240"/>
    </g>
  </svg>

  <div class="agent-photo" role="img" aria-label="Portrait photo of Marcus Pellton in a navy blazer and white shirt"></div>

  <h1 class="agent-name">Marcus Pellton</h1>
  <p class="agent-titles">Real Estate Professional<span class="sep">•</span>Buyer/Seller Specialist</p>

  <div class="contact-row row-phone">
    <svg viewBox="0 0 24 24" aria-hidden="true"><path fill="#0e2f5c" d="M6.6 2.2c.6-.3 1.3-.1 1.6.5l2 3.6c.3.6.2 1.2-.3 1.6L8.3 9.2c1.1 2.5 3.1 4.5 5.6 5.7l1.3-1.6c.4-.5 1.1-.6 1.6-.3l3.6 2c.6.3.8 1 .5 1.6l-1.2 2.4c-.4.8-1.3 1.3-2.2 1.1C9.9 18.9 5 14 3.3 6.4c-.2-.9.2-1.8 1-2.2z"/></svg>
    <span class="divider"></span>
    <span class="value"><span class="label">Call/Text</span>410-739-2184</span>
  </div>

  <div class="contact-row row-email">
    <svg viewBox="0 0 24 24" aria-hidden="true"><path fill="#ffffff" d="M2 4l20 9-11 2-3 6-1-8z"/></svg>
    <span class="divider"></span>
    <span class="value">Marcuspell@mailbrook.com</span>
  </div>

  <div class="contact-row row-web">
    <svg viewBox="0 0 24 24" aria-hidden="true"><g fill="none" stroke="#0e2f5c" stroke-width="2.2"><circle cx="12" cy="12" r="10"/><ellipse cx="12" cy="12" rx="4.5" ry="10"/><line x1="2" y1="12" x2="22" y2="12"/><line x1="12" y1="2" x2="12" y2="22"/><line x1="4" y1="7" x2="20" y2="7"/><line x1="4" y1="17" x2="20" y2="17"/></g></svg>
    <span class="divider"></span>
    <span class="value">www.harborcrewhomes.com</span>
  </div>

  <div class="brand-mark">
    <span class="dot"></span>
    <span class="brand-name">Harbor Crew</span>
  </div>

  <div class="office">
    <p class="office-team">The Harbor Crew</p>
    <p class="office-brokerage">at Keystone Real Estate</p>
    <p class="office-address">2847 W Larkmoor Rd, Bel Air, MD 21014</p>
    <p class="office-phone">833-555-0192</p>
  </div>

  <div class="footer-band"></div>
</main>
</body>
</html>
```